Specialised investor in e-mobility and energy wants business card design

We need a business card design that fits our existing corporate design. <The look and feel must be 'sharp'/'clean', dynamic, communicate momentum, professionalism etc (as one would imagine from a firm in the financial sector). We like the idea of a reverse-side of the card that includes the logo, and the name and contact details on the other. We expect the deliverable to be whatever format might be required to be able to get cards printed directly by a service such as marlo cards. Our website is www.obrel.finance

```html
<!DOCTYPE html>
<html lang="en">
<head>
<meta charset="utf-8">
<title>Obrel Capital — Business Card</title>
<link rel="stylesheet" href="https://fonts.googleapis.com/css2?family=Montserrat:wght@400;500;700;800&display=swap">
<style>
  :root {
    --backdrop: #d9d9d7;
    --paper: #ffffff;
    --forest: #2f5022;
    --leaf: #7ab648;
    --ink: #4a4a4a;
    --rule: #4f6b3d;
  }
  * { box-sizing: border-box; margin: 0; padding: 0; }
  html, body {
    width: 1200px; height: 801px; overflow: hidden;
    background: var(--backdrop);
    font-family: "Montserrat", sans-serif;
  }
  .sheet {
    position: relative; width: 1200px; height: 801px;
    display: flex; align-items: center; justify-content: center; gap: 48px;
  }
  .card {
    position: relative; width: 520px; height: 297px;
    border-bottom: 4px solid var(--leaf);
    box-shadow: 0 14px 30px rgba(0,0,0,0.18);
  }
  .card--front { background: var(--paper); }
  .card--back { background: var(--forest); display: flex; align-items: center; justify-content: center; }

  .brand { display: flex; align-items: center; gap: 10px; font-weight: 500; letter-spacing: 0.5px; white-space: nowrap; }
  .brand__mark { width: 12px; height: 12px; background: var(--leaf); }
  .card--front .brand { position: absolute; left: 36px; top: 128px; font-size: 27px; color: var(--forest); }
  .card--back .brand { font-size: 46px; color: var(--paper); gap: 16px; }
  .card--back .brand__mark { width: 18px; height: 18px; }

  .divider { position: absolute; left: 268px; top: 58px; width: 1px; height: 182px; background: var(--rule); }

  .details { position: absolute; left: 288px; top: 58px; color: var(--ink); font-size: 11.5px; line-height: 1.55; white-space: nowrap; }
  .details__name { font-size: 20px; font-weight: 800; color: var(--forest); line-height: 1.1; }
  .details__name span { color: var(--leaf); }
  .details__role { margin-bottom: 8px; }
  .details__address { margin-bottom: 8px; }
  .contact { list-style: none; }
  .contact li { display: flex; align-items: center; gap: 8px; }
  .contact svg { width: 11px; height: 11px; flex: none; }
</style>
</head>
<body>
<main class="sheet">
  <section class="card card--front" aria-label="Card front">
    <div class="brand"><span class="brand__mark"></span>Obrel Capital</div>
    <div class="divider"></div>
    <div class="details">
      <p class="details__name">Martin <span>Kessler</span></p>
      <p class="details__role">Director/Founder</p>
      <p class="details__address">58 Alder Row<br>Westvale Town AB 3120</p>
      <ul class="contact">
        <li>
          <svg viewBox="0 0 12 12" aria-hidden="true"><path fill="var(--leaf)" d="M2.5 1h2l1 2.6-1.3 1a6 6 0 0 0 3.2 3.2l1-1.3L11 7.5v2a1.5 1.5 0 0 1-1.5 1.5A8.5 8.5 0 0 1 1 2.5 1.5 1.5 0 0 1 2.5 1z"/></svg>
          123-408-2917
        </li>
        <li>
          <svg viewBox="0 0 12 12" aria-hidden="true"><rect x="0.5" y="2" width="11" height="8" rx="1" fill="var(--leaf)"/><path d="M1 2.6 6 6.5l5-3.9" stroke="#fff" stroke-width="1" fill="none"/></svg>
          info@obrel.finance
        </li>
        <li>
          <svg viewBox="0 0 12 12" aria-hidden="true"><circle cx="6" cy="6" r="5.5" fill="var(--leaf)"/><path d="M0.5 6h11M6 0.5c-2.2 2.5-2.2 8.5 0 11M6 0.5c2.2 2.5 2.2 8.5 0 11" stroke="#fff" stroke-width="0.8" fill="none"/></svg>
          www.obrel.finance
        </li>
      </ul>
    </div>
  </section>
  <section class="card card--back" aria-label="Card back">
    <div class="brand"><span class="brand__mark"></span>Obrel Capital</div>
  </section>
</main>
</body>
</html>
```